Wanderlark Gin - Bottle Label for a craft Gin about to be launched on the world from New Zealand

We are a start up craft distillery in New Zealand. We have developed a wonderful Gin using our own grain spirit and both traditional and New Zealand native botanicals (Manuka to be specific), chosen our bottle and the name "Wanderlark" and done a bit of amateur label design and now we are looking for someone to make it great.

Feel free to change up our amateur concept but give us something that will pop from the back bar and scream authenticity, craft and individuality.

The attached files give you the specifications of the bottle, our current concept for a Wanderlark label and an earlier concept drawing that gives an idea of where we are thinking the two labels should go on the front of the bottle.

Thanks, we look forward to your ideas!!

Target Market(s)

High end and craft Gin drinkers. Hipsters and cocktail barflys and their bar tenders and bar owners

Requirements
Must have
• Attractive individuality
Nice to have
• Coolness
Should not have
• Uncoolness

```html
<!DOCTYPE html>
<html lang="en">
<head>
<meta charset="utf-8">
<title>Wanderlark Gin – Wild Drift Label</title>
<link rel="stylesheet" href="https://fonts.googleapis.com/css2?family=Amatic+SC:wght@700&family=Kaushan+Script&display=swap">
<style>
  :root {
    --page: #ffffff;
    --cream: #e6e2c4;
    --cream-soft: #f3f1e4;
    --ink: #1c1c1c;
    --teal: #6ecbbf;
    --gold: #f5c21b;
    --white: #ffffff;
    --seed: #dcdcdc;
    --flag-red: #d2232a;
    --flag-blue: #1d3f8f;
  }
  * { margin: 0; padding: 0; box-sizing: border-box; }
  html, body { width: 927px; height: 1200px; overflow: hidden; background: var(--page); }
  body { -webkit-font-smoothing: antialiased; -moz-osx-font-smoothing: grayscale; }
  .canvas { position: relative; width: 927px; height: 1200px; }
  .label-shape { position: absolute; left: 0; top: 0; }
  .abs { position: absolute; left: 0; width: 927px; text-align: center; }

  .brand-name {
    top: 298px; font-family: "Amatic SC", sans-serif; font-weight: 700;
    font-size: 30px; line-height: 1; color: var(--white); letter-spacing: 1px;
  }
  .product-name {
    top: 350px; font-family: "Kaushan Script", cursive; font-size: 38px;
    color: var(--gold); line-height: 1;
  }
  .origin {
    top: 534px; font-family: "Amatic SC", sans-serif; font-weight: 700;
    font-size: 32px; color: var(--ink); display: flex; justify-content: center;
    align-items: center; gap: 6px; line-height: 1;
  }
  .flag-rule { width: 22px; height: 5px; border-top: 2px solid var(--flag-blue); border-bottom: 2px solid var(--flag-red); }
  .style-line {
    top: 568px; font-family: "Kaushan Script", cursive; font-size: 23px; line-height: 1.2; color: var(--ink);
  }
  .volume {
    top: 600px; font-family: "Amatic SC", sans-serif; font-weight: 700;
    font-size: 56px; color: var(--ink); line-height: 1;
  }
  .volume small { font-size: 36px; }

  .recipe-title {
    top: 757px; font-family: "Amatic SC", sans-serif; font-weight: 700;
    font-size: 30px; color: var(--white); line-height: 1;
  }
  .recipe-title .mark { color: var(--gold); font-size: 18px; vertical-align: middle; }
  .tasting {
    top: 806px; font-family: "Amatic SC", sans-serif; font-weight: 700;
    font-size: 25px; line-height: 26px; color: var(--white);
  }
  .tasting em { font-style: normal; color: var(--gold); }
  .strength {
    top: 962px; left: 356px; width: 212px; display: flex; justify-content: space-between;
    font-family: "Amatic SC", sans-serif; font-weight: 700; font-size: 26px; color: var(--white); line-height: 1;
  }
  .strength .item { border-bottom: 1px solid var(--cream); padding-bottom: 2px; }
  .strength .teal { color: var(--teal); }
  .strength sup { color: var(--gold); font-size: 15px; }
  .vintage {
    top: 1006px; font-family: "Amatic SC", sans-serif; font-weight: 700;
    font-size: 22px; line-height: 1; color: var(--ink);
  }
</style>
</head>
<body>
<main class="canvas">
  <svg class="label-shape" width="927" height="1200" viewBox="0 0 927 1200">
    <defs>
      <clipPath id="inner-field">
        <path d="M316 206 Q316 188 336 186 L592 186 Q612 188 612 206 L612 360 Q594 700 578 1034 L344 1034 Q328 700 316 360 Z"/>
      </clipPath>
    </defs>
    <path d="M304 200 Q304 176 330 174 L598 174 Q624 176 624 200 L624 360 Q604 700 588 1040 Q586 1046 578 1046 L342 1046 Q334 1046 334 1040 Q318 700 304 360 Z" fill="var(--cream)"/>
    <path d="M316 206 Q316 188 336 186 L592 186 Q612 188 612 206 L612 360 Q594 700 578 1034 L344 1034 Q328 700 316 360 Z" fill="var(--white)"/>
    <g clip-path="url(#inner-field)">
      <ellipse cx="545" cy="230" rx="48" ry="46" fill="var(--cream-soft)" role="img" aria-label="Faint line drawing of a manuka sprig"/>
      <ellipse cx="382" cy="520" rx="60" ry="58" fill="var(--cream-soft)" role="img" aria-label="Faint line drawing of manuka flowers"/>
      <ellipse cx="462" cy="1010" rx="110" ry="22" fill="var(--cream-soft)" role="img" aria-label="Faint line drawing of manuka branches"/>
    </g>
    <path d="M396 286 L532 286 L544 300 L580 300 L580 314 L600 314 L600 330 L614 330 L614 410 L600 410 L600 428 L580 428 L580 444 L560 444 L548 458 L532 458 Q480 462 462 500 Q446 462 394 458 L378 458 L366 444 L346 444 L346 428 L326 428 L326 410 L312 410 L312 330 L326 330 L326 314 L346 314 L346 300 L382 300 Z" fill="var(--teal)"/>
    <path d="M400 292 L528 292 L540 306 L574 306 L574 320 L594 320 L594 336 L608 336 L608 404 L594 404 L594 422 L574 422 L574 438 L556 438 L544 452 L530 452 Q478 456 462 490 Q448 456 396 452 L382 452 L370 438 L352 438 L352 422 L332 422 L332 404 L318 404 L318 336 L332 336 L332 320 L352 320 L352 306 L386 306 Z" fill="var(--ink)"/>
    <path d="M336 346 Q462 338 588 346 M336 394 Q462 402 588 394" stroke="var(--teal)" stroke-width="2" fill="none"/>
    <path d="M350 364 l10 10 M360 364 l-10 10 M562 366 l10 10 M572 366 l-10 10" stroke="var(--white)" stroke-width="3"/>
    <ellipse cx="462" cy="432" rx="24" ry="10" fill="var(--white)" role="img" aria-label="Small drawing of a manuka seed pod"/>
    <ellipse cx="462" cy="702" rx="44" ry="13" fill="var(--seed)" role="img" aria-label="Drawing of a pile of juniper and grain"/>
    <rect x="322" y="729" width="282" height="270" fill="var(--ink)"/>
    <path d="M354 746 L570 744 L562 768 L574 792 L362 794 L370 770 Z" fill="var(--teal)"/>
    <path d="M354 798 Q462 792 574 796" stroke="var(--white)" stroke-width="1.5" fill="none"/>
    <line x1="356" y1="948" x2="568" y2="948" stroke="var(--teal)" stroke-width="1.5"/>
  </svg>

  <div class="abs brand-name">WANDERLARK</div>
  <div class="abs product-name">Wild Drift</div>
  <div class="abs origin"><span class="flag-rule"></span>NEW ZEALAND<span class="flag-rule"></span></div>
  <div class="abs style-line">Small Batch Gin</div>
  <div class="abs volume">500 <small>ML</small></div>

  <div class="abs recipe-title"><span class="mark">×</span> RECIPE #3 <span class="mark">×</span></div>
  <p class="abs tasting">
    A CLASSICALLY INSPIRED GIN<br>
    WITH DEVELOPED <em>CITRUS NOTES</em><br>
    FROM THE <em>MANUKA BERRIES</em> FROM<br>
    <em>HARRIET'S MATES</em>, BEST WITH<br>
    EQUAL MIX OF SOME <em>FANCY TONIC</em>.
  </p>
  <div class="abs strength">
    <span class="item">84 <span class="teal">PROOF</span></span>
    <span class="item">42<sup>%</sup> ALC. BY VOL.</span>
  </div>
  <div class="abs vintage">– 2016 –</div>
</main>
</body>
</html>
```